Web Design Project

We need a web design company for a company based in London. We are an online minicab booking service that produces real time quotes on cab journey for consumers. Our colours are currently red and yellow, but do not need to stay that way; it's open to interpretation. Please avoid yellow and black as a colour combination. Our current site is: www.ridelark.co.uk We are looking for a new site to be user-friendly and easy to use, but more polished and professional looking, without using it usability and simplicity. We need to keep the booking capability on each page and it needs to draw in the user's eye. We need a site that is reliable and easy to use, but also fun.

Main objective: keep it simple, like it is now, but polish it up some. Also, we need to be able to add more content to it. And, we will also be adding a login capability for return users.

Target Market(s)

Internet-savvy people aged 18 and older.

Industry/Entity Type

It Company

Requirements
Must have
• Must have the booking widget. However, it doesn't have to be as large as it is now. We are actually thinking to split it over two pages. We will add a few options to the booking widget, such as another via option. The booking widget must be the most noticeable feature on the page. Sans serif font, please.
Should not have
• Should not be too busy and distracting. Please do not use any images of traditional taxis, ie. black cabs from London or yellow cabs from NYC. Our cars do not resemble these and our business cannot be associated with these images.

```html
<!DOCTYPE html>
<html lang="en">
<head>
<meta charset="utf-8">
<title>Ridelark – Order your cab online</title>
<link rel="stylesheet" href="https://fonts.googleapis.com/css2?family=Source+Sans+3:wght@400;600;700&display=swap">
<style>
:root{
  --red:#e01f2c;
  --red-deep:#b20f1a;
  --red-nav:#df1f2d;
  --maroon:#301a1b;
  --maroon-panel:#4b3132;
  --maroon-card:#5a3a3a;
  --maroon-dark:#1f0d0e;
  --muted-head:#b88a85;
  --label:#6d5152;
  --white:#ffffff;
  --footer-text:#8a0a12;
}
*{box-sizing:border-box;margin:0;padding:0}
html,body{width:1200px;height:1059px;overflow:hidden}
body{position:relative;background:var(--maroon);font-family:"Source Sans 3",sans-serif;color:var(--white)}
.abs{position:absolute}

/* header */
.site-header{position:absolute;left:0;top:0;width:1200px;height:99px;background:linear-gradient(#b4101a,#a30c15)}
.brand{left:38px;top:22px;font-size:48px;font-weight:700;color:var(--white);line-height:1;letter-spacing:-.5px}
.tagline{left:400px;top:54px;font-size:30px;font-weight:400;line-height:1;letter-spacing:.5px}
.driver-prompt{left:777px;top:17px;font-size:15px;font-weight:600}
.join-btn{left:1039px;top:14px;width:119px;height:26px;border-radius:8px;background:#2b1314;font-size:16px;text-align:center;line-height:25px}
.booking-line{left:737px;top:51px;width:439px;height:47px;background:var(--red);font-size:27px;font-weight:700;text-align:center;line-height:47px;letter-spacing:.6px}

/* nav */
.main-nav{position:absolute;left:0;top:99px;width:1200px;height:46px;background:var(--red-nav)}
.main-nav a{position:absolute;top:0;height:46px;line-height:46px;color:var(--white);text-decoration:none;font-size:15.5px;transform:translateX(-50%)}
.main-nav .current{left:579px;width:118px;text-align:center;background:linear-gradient(#d01521,#a50e18);box-shadow:inset 1px 0 #f04a54,inset -1px 0 #f04a54}

/* left column */
.intro-title{left:26px;top:164px;font-size:25px;color:var(--red);letter-spacing:.4px}
.intro-sub{left:26px;top:194px;font-size:16px}
.steps{left:22px;top:231px;list-style:none;font-size:16px;line-height:25px}
.steps li{padding-left:24px;position:relative}
.steps li svg{position:absolute;left:2px;top:8px}
.divider{left:24px;width:680px;height:1px;background:#0f0506}
.section-tab{left:24px;top:326px;width:222px;height:38px;background:var(--maroon-dark);color:var(--red);font-size:22px;line-height:38px;padding-left:14px}
.point{left:26px;width:680px}
.point h3{font-size:22px;font-weight:400;color:var(--muted-head);line-height:1.1}
.point p{font-size:15.5px;line-height:20px;margin-top:3px}
.testimonials-title{left:26px;top:622px;font-size:23px;color:var(--red);letter-spacing:.4px}
.testimonial{left:24px;width:311px;background:var(--maroon-card);font-size:14.5px;line-height:17.6px;padding:14px 12px 0 12px;letter-spacing:.3px}
.testimonial .more{position:absolute;right:16px;bottom:4px;font-size:13px;color:#b38d88}
.post-bar{left:24px;top:911px;width:311px;height:31px;background:var(--maroon-dark)}
.post-btn{left:233px;top:913px;width:98px;height:26px;background:var(--red);font-size:16px;text-align:center;line-height:26px}

.cab-photo{left:336px;top:612px;width:630px;height:394px;background:radial-gradient(ellipse 48% 46% at 48% 50%,#d9dcde 0%,#a9adb0 45%,rgba(60,40,40,.4) 80%,rgba(48,26,27,0) 100%)}

/* booking panel */
.booking-panel{left:737px;top:145px;width:439px;height:862px;background:var(--maroon-panel)}
.right-strip{left:1176px;top:145px;width:24px;height:862px;background:#2d1718}
.panel-title{left:764px;top:166px;font-size:24px;font-weight:700}
.field-label{left:764px;font-size:17px;color:var(--label)}
.field-label.light{color:#eadcdc}
.input{background:var(--white);height:35px}
.input .hint{font-size:14.5px;font-style:italic;color:#9a9a9a;line-height:35px;padding-left:12px;letter-spacing:.4px}
.find-btn{width:72px;height:35px;background:var(--red);font-size:20px;text-align:center;line-height:35px}
.check{width:17px;height:17px;background:var(--white)}
.small-label{font-size:15px}
.select{background:var(--white);height:28px}
.select svg{position:absolute;right:8px;top:9px}
.quote-btn{left:791px;top:945px;width:333px;height:41px;border-radius:21px;background:linear-gradient(#3c1d1e,#1e0b0c);box-shadow:0 2px 4px rgba(0,0,0,.5);font-size:17.5px;text-align:center;line-height:41px;letter-spacing:.6px}

/* footer */
.site-footer{position:absolute;left:0;top:1007px;width:1200px;height:52px;background:var(--red-deep)}
.site-footer p{position:absolute;left:26px;top:18px;font-size:13px;color:var(--footer-text)}
</style>
</head>
<body>

<header class="site-header">
  <div class="abs brand">Ridelark.co.uk</div>
  <div class="abs tagline">Order your cab online</div>
  <div class="abs driver-prompt">Are you a taxi driver or a company?</div>
  <div class="abs join-btn">Join Here</div>
  <div class="abs booking-line">Booking Line : 020 7946 0312</div>
</header>

<nav class="main-nav">
  <a class="current" href="#">Home</a>
  <a href="#" style="left:712px">Ridelark Miles</a>
  <a href="#" style="left:849px">Join Us</a>
  <a href="#" style="left:972px">About Us</a>
  <a href="#" style="left:1099px">Contact</a>
</nav>

<main>
  <h1 class="abs intro-title">As easy as opening the cab's door</h1>
  <p class="abs intro-sub">Its free, dependable and with no obligation</p>
  <ul class="abs steps">
    <li><svg width="10" height="9" viewBox="0 0 10 9"><path d="M0 3h5V0l5 4.5L5 9V6H0z" fill="#8c5b58"/></svg>Enter your route</li>
    <li><svg width="10" height="9" viewBox="0 0 10 9"><path d="M0 3h5V0l5 4.5L5 9V6H0z" fill="#8c5b58"/></svg>Quickly compare taxi fares</li>
    <li><svg width="10" height="9" viewBox="0 0 10 9"><path d="M0 3h5V0l5 4.5L5 9V6H0z" fill="#8c5b58"/></svg>Get your travel confirmed on your phone by SMS.</li>
  </ul>
  <div class="abs divider" style="top:324px"></div>

  <h2 class="abs section-tab">Why Ridelark ?</h2>
  <div class="abs point" style="top:374px"><h3>Price</h3><p>Ridelark guarantees that you get the best deal for your travel, as you get quotes from several cab companies.</p></div>
  <div class="abs point" style="top:454px"><h3>No fees</h3><p>There's absolutely no cost for you to use our service.</p></div>
  <div class="abs point" style="top:515px"><h3>Coverage</h3><p>Ridelark has the largest database of licensed minicab operators. You can use Ridelark wherever you are in greater London.</p></div>
  <div class="abs divider" style="top:601px"></div>

  <h2 class="abs testimonials-title">Testimonials</h2>
  <div class="abs testimonial" style="top:656px;height:120px">I recently hit London for a girlie night on the town with my bestie. After a little too much champagne, we had a stupid argument and decided to leave the club early......<span class="more">more</span></div>
  <div class="abs testimonial" style="top:778px;height:130px">I recently hit London for a girlie night on the town with my bestie. After a little too much champagne, we had a stupid argument and decided to leave the club early......<span class="more">more</span></div>
  <div class="abs post-bar"></div>
  <div class="abs post-btn">Post more</div>
</main>

<aside>
  <div class="abs booking-panel"></div>
  <div class="abs right-strip"></div>
  <div class="abs cab-photo" role="img" aria-label="Photo of a silver cab seen from the front"></div>

  <h2 class="abs panel-title">Book A Cab</h2>

  <div class="abs field-label" style="top:212px">Pick me up from:</div>
  <div class="abs input" style="left:765px;top:241px;width:309px"><div class="hint">address or post code</div></div>
  <div class="abs find-btn" style="left:1081px;top:241px">Find</div>
  <div class="abs check" style="left:765px;top:285px"></div>
  <div class="abs small-label" style="left:796px;top:283px">add via address:</div>

  <div class="abs field-label" style="top:316px">Drop me at:</div>
  <div class="abs input" style="left:765px;top:345px;width:309px"><div class="hint">address or post code</div></div>
  <div class="abs find-btn" style="left:1081px;top:345px">Find</div>

  <div class="abs field-label" style="top:388px">Pick up date and time:</div>
  <div class="abs input" style="left:765px;top:416px;width:309px"></div>
  <svg class="abs" style="left:1081px;top:415px" width="37" height="37" viewBox="0 0 37 37" aria-hidden="true">
    <rect x="1" y="3" width="35" height="33" fill="#eef2f8" stroke="#8aa2c4"/>
    <rect x="1" y="3" width="35" height="8" fill="#5d86c2"/>
    <g fill="#b9c8de">
      <rect x="5" y="14" width="5" height="4"/><rect x="12" y="14" width="5" height="4"/><rect x="19" y="14" width="5" height="4"/><rect x="26" y="14" width="5" height="4"/>
      <rect x="5" y="21" width="5" height="4"/><rect x="12" y="21" width="5" height="4"/><rect x="19" y="21" width="5" height="4"/><rect x="26" y="21" width="5" height="4"/>
      <rect x="5" y="28" width="5" height="4"/><rect x="12" y="28" width="5" height="4"/><rect x="19" y="28" width="5" height="4"/>
    </g>
  </svg>

  <div class="abs small-label" style="left:767px;top:466px">Just pick me up in</div>
  <div class="abs select" style="left:915px;top:464px;width:159px"><svg width="12" height="10" viewBox="0 0 12 10"><path d="M0 0h12L6 10z" fill="#222"/></svg></div>

  <div class="abs field-label" style="top:505px">Passengers:</div>
  <div class="abs select" style="left:765px;top:535px;width:84px;height:33px"><svg width="12" height="10" viewBox="0 0 12 10" style="top:12px"><path d="M0 0h12L6 10z" fill="#222"/></svg></div>
  <div class="abs small-label" style="left:856px;top:541px">Adults</div>
  <div class="abs select" style="left:914px;top:535px;width:85px;height:33px"><svg width="12" height="10" viewBox="0 0 12 10" style="top:12px"><path d="M0 0h12L6 10z" fill="#222"/></svg></div>
  <div class="abs small-label" style="left:1007px;top:541px">Bags</div>

  <div class="abs check" style="left:765px;top:594px"></div>
  <div class="abs field-label" style="left:806px;top:590px">Return Journey</div>
  <div class="abs check" style="left:765px;top:636px"></div>
  <div class="abs field-label" style="left:806px;top:632px">Extras</div>

  <div class="abs field-label light" style="top:703px">Mobile Number:</div>
  <div class="abs input" style="left:765px;top:729px;width:309px"></div>
  <div class="abs field-label light" style="top:774px">Email:</div>
  <div class="abs input" style="left:765px;top:801px;width:309px"></div>
  <div class="abs field-label light" style="top:845px">Comments:</div>
  <div class="abs input" style="left:765px;top:875px;width:309px"></div>

  <div class="abs quote-btn">Get Your No Obligation Quote</div>
</aside>

<footer class="site-footer">
  <p>2012 Ridelark | Company Info | Privacy Policy | Website by Brightfold Media - Release 1.1.0 (26-FEB-2012)</p>
</footer>

</body>
</html>
```